Label and packaging - Lune de Sable

We are after label and pack design for a product called Lune de Sable. This product is a blend of Pinot Gris and Apple Cider.

Lune de Sable:

The packaging needs to accomplish the following: quickly explain what the product is, establish as a premium price product and grab the eye. The package should also reflect the product innovation.

Quickly Explain What the Product Is:

Lune de Sable is a nice name that could lift the image – but no one will have any idea what the product is by the name. Consider that a consumer will be staring at a shelf, then the bottle for maybe two to three seconds before moving on to another bottle. In those three seconds we need to make certain that they understand that the product is a blend of wine and cider. Lune de Sable will not support this on its own.

Suggestion is to use words like Wine, Cider, Orchard, Vine, Apple, Heirloom, Exotic and make it simple. Perhaps a sticker that says “50% Wine/50% Apple Cider” that sits on the neck of every bottle. They need to quickly ‘get it”. Imagery will assist as well. Consider a hybrid 50/50 image of wine grapes and apples to tell the story.

Establish a Premium Price Point:

The label needs to say high quality in the package and the font. Have fun with the shipper – this is where you can have a field day with imagery and fun buzz words – we love the idea of a busy shipper that tells the story with a clean and smart looking bottle.

Target Market(s)

This is a premium product targeted at females of age 25-45.

Industry/Entity Type

Consumer

Colors
ec1f27
9bcb3c

Requirements
Must have
• Label design on a burgundy bottle with a screw cap, see here for bottle shape: http://www.vexlabottles.co.nz/wine/#/?view=thumbs&segments=41&colors=&capacityMin=187&capacityMax=750&heightMin=171&heightMax=334&labelMin=44&labelMax=168&neckMin=0&neckMax=1000

Packaging design on a 12 x 750ml carton. This sort of thing: https://www.brakunstores.com.au/images/photo06.jpg

Nice to have
• We have attached some examples of a concept we quite like but it's not bright enough.

```html
<!DOCTYPE html>
<html lang="en">
<head>
<meta charset="utf-8">
<title>Lune de Sable — Wine Label</title>
<link rel="stylesheet" href="https://fonts.googleapis.com/css2?family=EB+Garamond:ital,wght@0,400;0,500;1,400&display=swap">
<style>
  :root {
    --page: #f2f0ea;
    --ink: #1a1a17;
    --label-cream: #f6f1b8;
    --label-lime: #d9e27a;
    --label-olive: #b8c850;
    --gold-line: #c9a93a;
    --band-green: #4f8a2b;
    --band-text: #f4f6e4;
    --apple-red: #c8322a;
    --apple-green: #9bcb3c;
  }
  * { box-sizing: border-box; margin: 0; padding: 0; }
  html, body { width: 1200px; height: 737px; overflow: hidden; }
  body {
    background: var(--page);
    font-family: "EB Garamond", Garamond, serif;
    color: var(--ink);
    position: relative;
  }
  .label {
    position: absolute;
    left: 250px;
    top: 90px;
    width: 340px;
    height: 560px;
    background: linear-gradient(180deg, var(--label-cream) 0%, var(--label-lime) 55%, var(--label-olive) 100%);
    border: 2px solid var(--gold-line);
    box-shadow: 0 10px 30px rgba(0,0,0,0.12);
    padding: 14px;
  }
  .label__inner {
    height: 100%;
    border: 1px solid var(--gold-line);
    display: flex;
    flex-direction: column;
    align-items: center;
  }
  .label__name {
    margin-top: 40px;
    font-size: 40px;
    font-weight: 400;
    letter-spacing: 0.5px;
    color: var(--ink);
  }
  .label__band {
    margin-top: 22px;
    width: 100%;
    background: var(--band-green);
    color: var(--band-text);
    font-style: italic;
    font-size: 21px;
    line-height: 1.2;
    padding: 10px 0 10px 120px;
  }
  .label__photo {
    margin-top: 14px;
    width: 210px;
    height: 170px;
    border-radius: 6px;
    background: radial-gradient(circle at 40% 45%, var(--apple-red) 0%, #a6281f 45%, var(--apple-green) 85%);
  }
  .label__blend {
    margin-top: 28px;
    text-align: center;
    font-size: 19px;
    line-height: 1.35;
    color: var(--ink);
  }
  .wordmark {
    position: absolute;
    left: 700px;
    top: 300px;
    font-size: 60px;
    font-weight: 400;
    color: var(--ink);
    letter-spacing: 0.5px;
  }
</style>
</head>
<body>
  <section class="label" aria-label="Lune de Sable bottle label">
    <div class="label__inner">
      <h1 class="label__name">Lune de Sable</h1>
      <p class="label__band">50% Wine<br>50% Apple Cider</p>
      <div class="label__photo" role="img" aria-label="Photograph of a ripe red and green apple"></div>
      <p class="label__blend">Blend of New Zealand Pinot Gris<br>and Sparkling Apple Cider</p>
    </div>
  </section>
  <p class="wordmark">Lune de Sable</p>
</body>
</html>
```